Farm product labels

This is meant to design a set of labels for the following products:
Sachets (similar to Brindlecombe’s ketchup):
- Size: W4xH9 cm. This is the internal area (inside the four sealing borders) of sachets. Front side contains the design, and back side just texts with the ingredients, nutrition facts and origin. Please check check the attached pictures related to sachet designs for your reference!
- Products:
o Ketchup
o Honey
o Dulcevara (chocolate spread made of cacao, peanuts, and milk)
o Peanut butter
o Fruit jam (either Mango, Guava or Passion fruit)

Stickers (to be added on transparent bags):
- Size: W8xH14 cm. It does not need to be rectangular
- It needs to accommodate small texts with the ingredients, nutrition facts and origin
- Products:
o Tomato paste
o Fruit pulp (either Mango, Guava or Passion fruit)
o Processed vegetables (either Yuca or Sweet potato). They are peeled, chopped, pre-boiled and frozen.

For those interested I’ll provide detailed info as required

Target Market(s)

Hotels. The sachets are specially for breakfast

Requirements
Must have
• All product label designs should:
- Show a similar look, reflecting a single source/branding
- Be attractive and be easy to recognize each product
- Contain the logo of our farm (uploaded)

```html
<!DOCTYPE html>
<html lang="en">
<head>
<meta charset="utf-8">
<title>Verdella Farms – Sachet Labels</title>
<link rel="stylesheet" href="https://fonts.googleapis.com/css2?family=Archivo:wght@800&family=Arimo:wght@400;700&display=swap">
<style>
  :root{
    --bg:#cfe9ed;
    --white:#ffffff;
    --ink:#1c1c1c;
    --ketchup:#ef2b55;
    --honey:#f7ab4c;
    --choco:#8a4a40;
    --peanut:#f5813e;
    --jam:#bd68ef;
  }
  *{box-sizing:border-box;margin:0;padding:0}
  html,body{width:1200px;height:996px;overflow:hidden}
  body{background:var(--bg);position:relative;font-family:'Arimo',Arial,sans-serif;color:var(--ink)}

  .label-set{position:absolute;inset:0}
  .product{position:absolute;top:0;width:205px;height:996px}
  .ketchup{left:39px;--c:var(--ketchup)}
  .honey{left:277px;--c:var(--honey)}
  .choco{left:505px;--c:var(--choco)}
  .peanut{left:738px;--c:var(--peanut)}
  .jam{left:966px;--c:var(--jam)}

  /* front of sachet */
  .sachet-front{position:absolute;left:0;top:21px;width:205px;height:470px;background:var(--white)}
  .frame{position:absolute;left:14px;top:23px;width:150px;height:416px;border:3px solid var(--c)}
  .band{position:absolute;left:118px;top:11px;width:72px;height:418px;background:var(--c);
        display:flex;align-items:center;justify-content:center}
  .band::before{content:"";position:absolute;left:-7px;top:7px;width:72px;height:418px;background:var(--c);opacity:.45;z-index:-1}
  .product-name{writing-mode:vertical-rl;transform:rotate(180deg);color:var(--white);
        font-family:'Archivo',Arial,sans-serif;font-weight:800;font-size:29px;letter-spacing:1px;
        line-height:1.05;text-align:center;white-space:nowrap}
  .product-name small{display:block;font-size:19px;letter-spacing:.5px}
  .brand{position:absolute;left:26px;top:150px;width:80px;display:flex;flex-direction:column;align-items:center;gap:6px;color:var(--c)}
  .brand-dot{width:34px;height:34px;border-radius:50%;background:var(--c)}
  .brand-name{font-family:'Arimo',Arial,sans-serif;font-weight:700;font-size:12px;letter-spacing:.5px}

  /* back of sachet */
  .sachet-back{position:absolute;left:0;top:509px;width:205px;height:470px;background:var(--c)}
  .nutrition{position:absolute;left:14px;top:27px;width:178px;height:310px;background:var(--white);padding:8px 10px;font-size:8px;line-height:11.2px}
  .nutrition h2{font-size:19px;line-height:22px;font-weight:700;border-bottom:1px solid var(--ink);padding-bottom:2px;margin-bottom:2px}
  .row{display:flex;justify-content:space-between;font-weight:700}
  .row.sub{padding-left:10px;font-weight:400}
  .row.light{font-weight:400}
  .rule{border-top:1px solid var(--ink);margin:2px 0}
  .rule.thick{border-top-width:4px}
  .dv{text-align:right;font-size:6.5px}
  .footnote{font-size:5.5px;line-height:7px;margin-top:4px}
  .ingredients{position:absolute;left:14px;top:372px;color:var(--white);font-size:17px}
  .write-line{position:absolute;left:14px;width:176px;border-top:1.5px solid var(--white);opacity:.9}
  .l1{top:414px}.l2{top:432px}.l3{top:450px}
</style>
</head>
<body>
<main class="label-set">

<section class="product ketchup">
  <div class="sachet-front">
    <div class="frame"></div>
    <div class="brand"><span class="brand-dot"></span><span class="brand-name">VERDELLA</span></div>
    <div class="band"><h1 class="product-name">TOMATO KETCHUP</h1></div>
  </div>
  <div class="sachet-back">
    <div class="nutrition">
      <h2>Nutrition Facts</h2>
      <div class="row light"><span>Serving Size</span><span>...g</span></div>
      <div class="row light"><span>Servings Per Container</span></div>
      <div class="rule thick"></div>
      <div class="row"><span>Amount Per Serving</span></div>
      <div class="row"><span>Calories ...</span><span>Calories from Fat ...</span></div>
      <div class="dv">% Daily Value*</div>
      <div class="rule"></div>
      <div class="row"><span>Total Fat ...g</span><span>...%</span></div>
      <div class="row sub"><span>Saturated Fat ...g</span><span>...%</span></div>
      <div class="row sub"><span>Trans Fat ...g</span></div>
      <div class="row"><span>Cholesterol ...mg</span><span>...%</span></div>
      <div class="row"><span>Sodium ...mg</span><span>...%</span></div>
      <div class="row"><span>Total Carbohydrate ...g</span><span>...%</span></div>
      <div class="row sub"><span>Dietary Fiber ...g</span><span>...%</span></div>
      <div class="row sub"><span>Sugars ...g</span></div>
      <div class="row"><span>Protein ...g</span></div>
      <div class="rule thick"></div>
      <div class="row light"><span>Vitamin A</span><span>...%</span></div>
      <div class="row light"><span>Vitamin C</span><span>...%</span></div>
      <div class="row light"><span>Calcium</span><span>...%</span></div>
      <div class="row light"><span>Iron</span><span>...%</span></div>
      <p class="footnote">*Percent Daily Values are based on a 2,000 calorie diet. Your daily values may be higher or lower depending on your calorie needs.</p>
    </div>
    <p class="ingredients">ingredientsingredients</p>
    <span class="write-line l1"></span><span class="write-line l2"></span><span class="write-line l3"></span>
  </div>
</section>

<section class="product honey">
  <div class="sachet-front">
    <div class="frame"></div>
    <div class="brand"><span class="brand-dot"></span><span class="brand-name">VERDELLA</span></div>
    <div class="band"><h1 class="product-name">HONEY</h1></div>
  </div>
  <div class="sachet-back">
    <div class="nutrition">
      <h2>Nutrition Facts</h2>
      <div class="row light"><span>Serving Size</span><span>...g</span></div>
      <div class="row light"><span>Servings Per Container</span></div>
      <div class="rule thick"></div>
      <div class="row"><span>Amount Per Serving</span></div>
      <div class="row"><span>Calories ...</span><span>Calories from Fat ...</span></div>
      <div class="dv">% Daily Value*</div>
      <div class="rule"></div>
      <div class="row"><span>Total Fat ...g</span><span>...%</span></div>
      <div class="row sub"><span>Saturated Fat ...g</span><span>...%</span></div>
      <div class="row sub"><span>Trans Fat ...g</span></div>
      <div class="row"><span>Cholesterol ...mg</span><span>...%</span></div>
      <div class="row"><span>Sodium ...mg</span><span>...%</span></div>
      <div class="row"><span>Total Carbohydrate ...g</span><span>...%</span></div>
      <div class="row sub"><span>Dietary Fiber ...g</span><span>...%</span></div>
      <div class="row sub"><span>Sugars ...g</span></div>
      <div class="row"><span>Protein ...g</span></div>
      <div class="rule thick"></div>
      <div class="row light"><span>Vitamin A</span><span>...%</span></div>
      <div class="row light"><span>Vitamin C</span><span>...%</span></div>
      <div class="row light"><span>Calcium</span><span>...%</span></div>
      <div class="row light"><span>Iron</span><span>...%</span></div>
      <p class="footnote">*Percent Daily Values are based on a 2,000 calorie diet. Your daily values may be higher or lower depending on your calorie needs.</p>
    </div>
    <p class="ingredients">ingredientsingredients</p>
    <span class="write-line l1"></span><span class="write-line l2"></span><span class="write-line l3"></span>
  </div>
</section>

<section class="product choco">
  <div class="sachet-front">
    <div class="frame"></div>
    <div class="brand"><span class="brand-dot"></span><span class="brand-name">VERDELLA</span></div>
    <div class="band"><h1 class="product-name">DULCEVARA<small>CHOCOLAE SPREAD</small></h1></div>
  </div>
  <div class="sachet-back">
    <div class="nutrition">
      <h2>Nutrition Facts</h2>
      <div class="row light"><span>Serving Size</span><span>...g</span></div>
      <div class="row light"><span>Servings Per Container</span></div>
      <div class="rule thick"></div>
      <div class="row"><span>Amount Per Serving</span></div>
      <div class="row"><span>Calories ...</span><span>Calories from Fat ...</span></div>
      <div class="dv">% Daily Value*</div>
      <div class="rule"></div>
      <div class="row"><span>Total Fat ...g</span><span>...%</span></div>
      <div class="row sub"><span>Saturated Fat ...g</span><span>...%</span></div>
      <div class="row sub"><span>Trans Fat ...g</span></div>
      <div class="row"><span>Cholesterol ...mg</span><span>...%</span></div>
      <div class="row"><span>Sodium ...mg</span><span>...%</span></div>
      <div class="row"><span>Total Carbohydrate ...g</span><span>...%</span></div>
      <div class="row sub"><span>Dietary Fiber ...g</span><span>...%</span></div>
      <div class="row sub"><span>Sugars ...g</span></div>
      <div class="row"><span>Protein ...g</span></div>
      <div class="rule thick"></div>
      <div class="row light"><span>Vitamin A</span><span>...%</span></div>
      <div class="row light"><span>Vitamin C</span><span>...%</span></div>
      <div class="row light"><span>Calcium</span><span>...%</span></div>
      <div class="row light"><span>Iron</span><span>...%</span></div>
      <p class="footnote">*Percent Daily Values are based on a 2,000 calorie diet. Your daily values may be higher or lower depending on your calorie needs.</p>
    </div>
    <p class="ingredients">ingredientsingredients</p>
    <span class="write-line l1"></span><span class="write-line l2"></span><span class="write-line l3"></span>
  </div>
</section>

<section class="product peanut">
  <div class="sachet-front">
    <div class="frame"></div>
    <div class="brand"><span class="brand-dot"></span><span class="brand-name">VERDELLA</span></div>
    <div class="band"><h1 class="product-name">PEANUT BUTTER</h1></div>
  </div>
  <div class="sachet-back">
    <div class="nutrition">
      <h2>Nutrition Facts</h2>
      <div class="row light"><span>Serving Size</span><span>...g</span></div>
      <div class="row light"><span>Servings Per Container</span></div>
      <div class="rule thick"></div>
      <div class="row"><span>Amount Per Serving</span></div>
      <div class="row"><span>Calories ...</span><span>Calories from Fat ...</span></div>
      <div class="dv">% Daily Value*</div>
      <div class="rule"></div>
      <div class="row"><span>Total Fat ...g</span><span>...%</span></div>
      <div class="row sub"><span>Saturated Fat ...g</span><span>...%</span></div>
      <div class="row sub"><span>Trans Fat ...g</span></div>
      <div class="row"><span>Cholesterol ...mg</span><span>...%</span></div>
      <div class="row"><span>Sodium ...mg</span><span>...%</span></div>
      <div class="row"><span>Total Carbohydrate ...g</span><span>...%</span></div>
      <div class="row sub"><span>Dietary Fiber ...g</span><span>...%</span></div>
      <div class="row sub"><span>Sugars ...g</span></div>
      <div class="row"><span>Protein ...g</span></div>
      <div class="rule thick"></div>
      <div class="row light"><span>Vitamin A</span><span>...%</span></div>
      <div class="row light"><span>Vitamin C</span><span>...%</span></div>
      <div class="row light"><span>Calcium</span><span>...%</span></div>
      <div class="row light"><span>Iron</span><span>...%</span></div>
      <p class="footnote">*Percent Daily Values are based on a 2,000 calorie diet. Your daily values may be higher or lower depending on your calorie needs.</p>
    </div>
    <p class="ingredients">ingredientsingredients</p>
    <span class="write-line l1"></span><span class="write-line l2"></span><span class="write-line l3"></span>
  </div>
</section>

<section class="product jam">
  <div class="sachet-front">
    <div class="frame"></div>
    <div class="brand"><span class="brand-dot"></span><span class="brand-name">VERDELLA</span></div>
    <div class="band"><h1 class="product-name">PASSION FRUIT<br>JAM</h1></div>
  </div>
  <div class="sachet-back">
    <div class="nutrition">
      <h2>Nutrition Facts</h2>
      <div class="row light"><span>Serving Size</span><span>...g</span></div>
      <div class="row light"><span>Servings Per Container</span></div>
      <div class="rule thick"></div>
      <div class="row"><span>Amount Per Serving</span></div>
      <div class="row"><span>Calories ...</span><span>Calories from Fat ...</span></div>
      <div class="dv">% Daily Value*</div>
      <div class="rule"></div>
      <div class="row"><span>Total Fat ...g</span><span>...%</span></div>
      <div class="row sub"><span>Saturated Fat ...g</span><span>...%</span></div>
      <div class="row sub"><span>Trans Fat ...g</span></div>
      <div class="row"><span>Cholesterol ...mg</span><span>...%</span></div>
      <div class="row"><span>Sodium ...mg</span><span>...%</span></div>
      <div class="row"><span>Total Carbohydrate ...g</span><span>...%</span></div>
      <div class="row sub"><span>Dietary Fiber ...g</span><span>...%</span></div>
      <div class="row sub"><span>Sugars ...g</span></div>
      <div class="row"><span>Protein ...g</span></div>
      <div class="rule thick"></div>
      <div class="row light"><span>Vitamin A</span><span>...%</span></div>
      <div class="row light"><span>Vitamin C</span><span>...%</span></div>
      <div class="row light"><span>Calcium</span><span>...%</span></div>
      <div class="row light"><span>Iron</span><span>...%</span></div>
      <p class="footnote">*Percent Daily Values are based on a 2,000 calorie diet. Your daily values may be higher or lower depending on your calorie needs.</p>
    </div>
    <p class="ingredients">ingredientsingredients</p>
    <span class="write-line l1"></span><span class="write-line l2"></span><span class="write-line l3"></span>
  </div>
</section>

</main>
</body>
</html>
```